Leadership/Education Book Cover Project

I need a book cover design for a new book titled "Purposeful Equity Stewardship: Sparking Renewal and Growth in Tertiary Learning."

This book is written to be a Tide Turner! Hence I need a game changing design!

The focus of the book is to help colleges and universities to build sustainable capacity to become more diverse (race, ethnicity, nationality, gender, sexual orientation), embrace diversity, and prepare all students irrespective of background for a world that is diverse, global, and interconnected.

I am looking for an "elegant" highly professional design that is directed towards leaders of organizations. Presidents, chief diversity officers, vice presidents, faculty - the goal is for the design to sell concepts like - professional, leadership, strategic, clear, organizational change management, planning, focus, discipline, etc - these are the lead themes - diversity is the issue, but I need to position this as an organizational change, management book for higher education audiences.

Less is more - as I am most looking for a typographic design theme, more than an image based design. At the same time, I am not opposed to having a design that includes some type of graphic elements that capture the key ideas.

No typical "diversity images" like hands, rainbows, etc. It has to be more sophisticated than that if your going to use images - also no people. No smiling multicultural faces. This is a business, management, leadership book - that is meant to be the definitive contribution of it's kind. Some models might include - Tide Turner, Solid to Stellar, 17 Pillars of Stewardship, Ripple, Drifters, The Craft of Oversight, Winning the Open Field, Charting New Waters, and The Stalled Campus Years.

At the same time, don't feel limited to these exact executions. I am open to some exploration of possibilities.

My color - taste is open, but the key is professional colors - nothing outlandish - nothing to bold. More subdued - as I am trying to find an image that suggests this is the best, most trust - worthy book ever written that can help you to manage your strategic diversity issues of access, inclusion, learning, etc - this book can help you to be more relevant and vibrant in the 21st Century Knowledge Economy.

If you use images - go deep into the concepts I offer here - don't live a the surface of the word diversity.

Here is some additional information about the book:

The Case for Merit: Purposeful Equity Stewardship on the Quad
By
Dr. Marcus T. Halvorsen & Dr. Lorna J. Pettigrew-Ashby
Quillmark Publishing Press
Anticipated Publication January 2012

This book, Purposeful Equity Stewardship: Sparking Renewal and Growth in Tertiary Learning focuses squarely on the topic of managing diversity in a higher education context. In doing this, it challenges the higher education community and others, to face what Neil Faraday, noted author of the book on excellence, Solid To Stellar, refers to as the brutal facts of their reality. Namely, that diversity is no longer simply a question of moral and social responsibility, but a matter of excellence. A matter of enhancing organizational creativity, learning, problem solving, and institutional effectiveness - - a matter of sustainability and maintaining global competitiveness in a 21st Century global knowledge economy.

Over the past century, American higher education has evolved dramatically. Once a privilege reserved for the elite, it has become a requirement for the majority. No longer the ivory tower, colleges and universities must be catalysts of economic development, laboratories for big ideas, and incubators of diverse leaders who champion the promise of American Democracy in the new economy. An economy where computer geeks rule and innovation eats orthodoxy, higher education is the key to our present and our future.

Issues of access, equity, and inclusion, matters of diversity must live in the foreground of institutional life. Nearly every great national challenge — from the search for clean energy, to the need for a new generation of scientists, depends on higher education and the benefits of diversity. Computer labs and internet workspaces are what assembly lines and automotive plants were 100 years ago-the drivers of growth in both good and bad times. Spaces where people must come together, collaborate, and harness the power of difference towards creative goals in a fast past and changing world.
A New Vision for Higher Education

Changing demographics, the emergence of a knowledge-based economy, chronic social inequities, a focus on the educational benefits of diverse learning environments, and workforce demands for graduates prepared to lead and follow in a global and interconnected world mandates a new approach to issues of diversity. An approach where our efforts are grounded in empirical evidence and best-practice efforts to achieve changes that are more than symbolic. Change that is not held hostage by personal anecdotes and the whims of leaders who have little experience with matters of institutional transformation, and even less experience leading these conversations around matters of diversity.

Now more than ever before, educational leaders need to ask themselves what are the big picture 21st century issues of diversity? What dynamics both constrain and enable our diversity agenda? In fact, how do we define diversity in the new millennium? Why was our diversity plan less than successful? What strategies do we have in place to advance diversity issues on campus? Are we at threat of being sued? Is diversity operating at a high enough level on campus? How should we track and define diversity in the new millennium? Do we need a chief diversity officer? If so, at what level of rank? Who should they supervise? Is diversity consistently on our agenda in the president’s cabinet, on the floor of faculty senate, or in the various school, college and divisional departments that exist across campus? Are we our own worse enemy? These are questions that institutional leaders have to ask themselves. To do anything less, is to simply throw money at a problem, or replay the same broken record without any new actions designed to break the cycle of failure, exclusion, and deprivation, echoing the clinical definition of insanity – repeating the same actions over and over again, expecting a new result!

In the world we live in today, diversity is not just the right thing to do- - it is the only thing to do. More than anecdotes and lived experiences, this book delivers theoretical and empirically grounded advice for institutions attempting to enhance their strategic capabilities by developing, optimizing, and better understanding the various diversity efforts that exist at their schools. Indeed in this book, we spend an entire chapter, embracing the complexity and challenge of defining diversity in a world in which race, ethnicity, gender, sexuality, nationality, and a host of other identities are all potentially tantamount to an institution’s definition and activation of the diversity idea on campuses big and small, rural and urban, private and public.

Not just a book for Chief Diversity Officers (CDO) or diversity professionals, this book is intended for ‘diversity champions’ who want to become strategic diversity leaders in the academy. A term we use to broadly refer to anyone involved in facilitating, initiating, influencing, or implementing diversity themed projects, or initiatives, whether or not they have an official title recognizing that responsibility or not. More than a how-to guide, this book is about both the process of leading diversity themed change, as well as the nature of diversity themed change in the academy. It presents a range of models, strategies, and contingencies that must be considered whether the goal is developing a rationale for campus diversity, building a new chief diversity officer role, reorganizing the current campus diversity infrastructure, developing a new diversity plan, defining diversity, or assessing the diversity process and journey of change. As a result, it has utility for anyone, regardless of role, who is interested in the process of strategic diversity leadership.

Book should be "single author" - Dr. Marcus T. Halvorsen

Designers -

I have posted some additional information that may enhance "text" driven design concepts.  It's information for using wordle - to generate concepts.  I have included:

(1) PES - text for drop into wordle
(2) PES - guide to give you settings for wordle
(3) Wordle - example of a pdf I like

You can feel free to use these to generate/revise concepts.  All other aspects of the brief still hold.

MTH

Reason: Designers - my apologies - I had a family situation - and was totally out of commission - I appreciate your patience - and plan to move forward.

The book will ultimately be 6 x 9 inches

mth

College and university presidents, senior leaders in higher education, faculty, chief diversity officers, business leaders - professionals

• The book must have the full title:

Purposeful Equity Stewardship:
Sparking Renewal and Growth in Tertiary Learning

Author:
Marcus T. Halvorsen, PhD
• No - obvious diversity references - hands, globes, diverse people, rainbows, etc - the focus is on "strategic diversity leadership" attempting to usher in a bold new paradigm centered on the idea that issues of diversity, equity, and inclusion - are key to the economic viability of the nation in a new global knowledge economy. That it's only being intentional in our efforts, to embrace diverse people, ideas, perspectives, etc - that we can become stronger as a nation.

```html
<!DOCTYPE html>
<html lang="en">
<head>
<meta charset="utf-8">
<title>Purposeful Equity Stewardship — Book Cover</title>
<link rel="stylesheet" href="https://fonts.googleapis.com/css2?family=Roboto:wght@700;900&family=Roboto+Condensed:wght@700&display=swap">
<style>
  :root {
    --cover-red: #a8262b;
    --paper: #ffffff;
    --ink-dark: #2a2a2a;
    --ink-mid: #555555;
    --ink-light: #9c9c9c;
  }
  html, body {
    margin: 0;
    padding: 0;
    width: 800px;
    height: 1200px;
    overflow: hidden;
    background: var(--paper);
  }
  .cover {
    position: relative;
    width: 800px;
    height: 1200px;
    background: var(--paper);
    overflow: hidden;
  }
  .title-band {
    position: absolute;
    left: 0; top: 0;
    width: 800px;
    height: 500px;
    background: var(--cover-red);
    display: flex;
    flex-direction: column;
    align-items: center;
    justify-content: center;
    gap: 6px;
  }
  .title-line {
    margin: 0;
    font-family: "Roboto", Arial, sans-serif;
    font-weight: 700;
    font-size: 64px;
    line-height: 108px;
    letter-spacing: 3px;
    color: var(--paper);
    text-transform: uppercase;
  }
  .subtitle {
    position: absolute;
    left: 0; top: 0;
    width: 800px;
    height: 1200px;
    margin: 0;
    font-family: "Roboto Condensed", "Arial Narrow", sans-serif;
    font-weight: 700;
    line-height: 1;
  }
  .subtitle span { position: absolute; white-space: nowrap; }
  .word-sparking   { left: 253px; top: 645px; font-size: 64px; color: var(--ink-dark); }
  .word-amp        { left: 485px; top: 608px; font-size: 128px; color: var(--cover-red); }
  .word-renewal    { left: 253px; top: 712px; font-size: 64px; color: var(--cover-red); }
  .word-growth     { left: 253px; top: 777px; font-size: 64px; color: var(--ink-mid); }
  .word-in         { left: 250px; top: 820px; font-size: 150px; color: var(--ink-light); letter-spacing: -2px; }
  .word-tertiary   { left: 348px; top: 848px; font-size: 60px; color: var(--cover-red); }
  .word-learning   { left: 348px; top: 906px; font-size: 60px; color: var(--ink-dark); }
  .author-band {
    position: absolute;
    left: 0; bottom: 0;
    width: 800px;
    height: 106px;
    background: var(--cover-red);
    display: flex;
    align-items: center;
    justify-content: center;
  }
  .author-name {
    margin: 0;
    font-family: "Roboto", Arial, sans-serif;
    font-weight: 700;
    font-size: 30px;
    letter-spacing: 0.5px;
    color: var(--paper);
  }
</style>
</head>
<body>
  <main class="cover">
    <header class="title-band">
      <h1 class="title-line">Purposeful</h1>
      <p class="title-line">Equity</p>
      <p class="title-line">Stewardship</p>
    </header>

    <h2 class="subtitle" aria-label="Sparking Renewal and Growth in Tertiary Learning">
      <span class="word-sparking">Sparking</span>
      <span class="word-amp">&amp;</span>
      <span class="word-renewal">Renewal</span>
      <span class="word-growth">Growth</span>
      <span class="word-in">in</span>
      <span class="word-tertiary">TERTIARY</span>
      <span class="word-learning">Learning</span>
    </h2>

    <footer class="author-band">
      <p class="author-name">Dr. Marcus T. Halvorsen</p>
    </footer>
  </main>
</body>
</html>
```